I need the below text put into an illustration/high res image so I can print out and frame and give to my fiance. Can be simple but must look elegant. Idea is that the text can be written in the sand on the attached pics (let me know if you require more high res). Not precious on the dimensions but think no more than 90cm length or width. Can be smaller whatever you think works best. You can half long sentences if you think it will look better.
Update: some of you asked for a picture of us, not sure it works but have attached one
Marriage
Marriage isn’t for you.
You don’t marry to make yourself happy, you marry to make someone else happy.
More than that, your marriage isn’t for yourself, you’re marrying for a family.
Not just for the in-laws and all of that nonsense, but for your future children.
Who do you want to help you raise them?
Who do you want to influence them?
Marriage isn’t for you.
It’s not about you.
Marriage is about the person you married.

```html
<!DOCTYPE html>
<html lang="en">
<head>
<meta charset="utf-8">
<title>Marriage isn’t for you — three finishes</title>
<link rel="stylesheet" href="https://fonts.googleapis.com/css2?family=Lobster&family=Lobster+Two:ital@1&family=Pinyon+Script&display=swap">
<style>
  :root {
    --backdrop: #2e2e2e;
    --ink: #2a2b22;
    --ink-formal: #17130b;
    --frame: #2f3430;
    --sea-sky: #bfe0e6;
    --sea-water: #8ec3c8;
    --sand-glow-cool: #eef2b6;
    --sand-edge-cool: #6da6a3;
    --sand-glow-warm: #f3e57a;
    --sand-mid-warm: #c9a24e;
    --sand-edge-warm: #7d4a1c;
    --rose-tone-light: rgba(236, 238, 214, 0.55);
    --rose-tone-green: rgba(120, 150, 96, 0.35);
  }
  * { margin: 0; padding: 0; box-sizing: border-box; }
  html, body { width: 758px; height: 1200px; overflow: hidden; background: var(--backdrop); }
  .sheet { position: relative; width: 758px; height: 1200px; }

  .print {
    position: absolute;
    left: 162px;
    width: 454px;
    height: 375px;
    overflow: hidden;
    box-shadow: 0 0 0 1px #1c1c1c;
  }
  .print--lobster { top: 29px; }
  .print--italic  { top: 409px; }
  .print--formal  { top: 789px; }

  .beach-photo { position: absolute; inset: 0; }
  .print--lobster .beach-photo,
  .print--italic .beach-photo {
    background:
      linear-gradient(180deg, var(--sea-sky) 0%, var(--sea-water) 9%, rgba(142,195,200,0) 20%),
      linear-gradient(120deg, rgba(200,230,232,.75) 0%, rgba(200,230,232,0) 35%),
      radial-gradient(ellipse 62% 58% at 58% 50%, var(--sand-glow-cool) 0%, #dfe8a8 45%, var(--sand-edge-cool) 100%);
  }
  .print--formal .beach-photo {
    background:
      linear-gradient(180deg, #b9cfe0 0%, #9fb7bf 8%, rgba(160,180,185,0) 18%),
      linear-gradient(120deg, rgba(222,228,220,.8) 0%, rgba(222,228,220,0) 33%),
      radial-gradient(ellipse 58% 54% at 60% 50%, var(--sand-glow-warm) 0%, #dcbc60 50%, var(--sand-edge-warm) 100%);
  }

  .frame { position: absolute; inset: 0; width: 454px; height: 375px; }
  .frame rect, .frame line { fill: none; stroke: var(--frame); }

  .rose-photo {
    position: absolute;
    left: 146px; top: 304px;
    width: 82px; height: 38px;
    border-radius: 3px;
    background: linear-gradient(135deg, var(--rose-tone-light) 0%, var(--rose-tone-green) 100%);
  }

  .verse {
    position: absolute;
    left: 14px; right: 14px;
    list-style: none;
    text-align: center;
    color: var(--ink);
  }
  .print--lobster .verse {
    top: 80px;
    font-family: "Lobster", cursive;
    font-size: 11.9px;
    line-height: 20.6px;
  }
  .print--italic .verse {
    top: 81px;
    font-family: "Lobster Two", cursive;
    font-style: italic;
    font-size: 11.9px;
    line-height: 20.6px;
  }
  .print--formal .verse {
    top: 65px;
    font-family: "Pinyon Script", cursive;
    font-size: 11px;
    line-height: 24.2px;
    color: var(--ink-formal);
    text-shadow: 0 0 0.4px var(--ink-formal);
  }
</style>
</head>
<body>
<main class="sheet">

  <section class="print print--lobster">
    <div class="beach-photo" role="img" aria-label="Photo of a quiet sandy beach with sea and a headland on the horizon"></div>
    <svg class="frame" viewBox="0 0 454 375" aria-hidden="true">
      <rect x="11" y="11" width="432" height="353" stroke-width="1.2"/>
      <rect x="16.5" y="16.5" width="421" height="342" stroke-width="0.8"/>
      <line x1="124" y1="43" x2="330" y2="43" stroke-width="1.6"/>
      <line x1="124" y1="320" x2="330" y2="320" stroke-width="1.6"/>
    </svg>
    <div class="rose-photo" role="img" aria-label="Photo of a single white rose lying on the sand"></div>
    <ul class="verse">
      <li>Marriage isn’t for you.</li>
      <li>You don’t marry to make yourself happy, you marry to make someone else happy.</li>
      <li>More than that, your marriage isn’t for yourself, you’re marrying for a family.</li>
      <li>Not just for the in-laws and all of that nonsense, but for your future children.</li>
      <li>Who do you want to help you raise them?</li>
      <li>Who do you want to influence them?</li>
      <li>Marriage isn’t for you.</li>
      <li>It’s not about you.</li>
      <li>Marriage is about the person you married.</li>
    </ul>
  </section>

  <section class="print print--italic">
    <div class="beach-photo" role="img" aria-label="Photo of a quiet sandy beach with sea and a headland on the horizon"></div>
    <svg class="frame" viewBox="0 0 454 375" aria-hidden="true">
      <rect x="11" y="11" width="432" height="353" stroke-width="1.2"/>
      <rect x="16.5" y="16.5" width="421" height="342" stroke-width="0.8"/>
      <line x1="124" y1="44" x2="330" y2="44" stroke-width="1.6"/>
      <line x1="124" y1="320" x2="330" y2="320" stroke-width="1.6"/>
    </svg>
    <div class="rose-photo" role="img" aria-label="Photo of a single white rose lying on the sand"></div>
    <ul class="verse">
      <li>Marriage isn’t for you.</li>
      <li>You don’t marry to make yourself happy, you marry to make someone else happy.</li>
      <li>More than that, your marriage isn’t for yourself, you’re marrying for a family.</li>
      <li>Not just for the in-laws and all of that nonsense, but for your future children.</li>
      <li>Who do you want to help you raise them?</li>
      <li>Who do you want to influence them?</li>
      <li>Marriage isn’t for you.</li>
      <li>It’s not about you.</li>
      <li>Marriage is about the person you married.</li>
    </ul>
  </section>

  <section class="print print--formal">
    <div class="beach-photo" role="img" aria-label="Photo of a golden sandy beach with sea and a headland on the horizon"></div>
    <svg class="frame" viewBox="0 0 454 375" aria-hidden="true">
      <rect x="11" y="11" width="432" height="353" stroke-width="1.2"/>
      <rect x="16.5" y="16.5" width="421" height="342" stroke-width="0.8"/>
      <line x1="124" y1="43" x2="330" y2="43" stroke-width="1.6"/>
      <line x1="124" y1="321" x2="330" y2="321" stroke-width="1.6"/>
    </svg>
    <div class="rose-photo" role="img" aria-label="Photo of a single white rose lying on the sand"></div>
    <ul class="verse">
      <li>Marriage isn’t for you.</li>
      <li>You don’t marry to make yourself happy, you marry to make someone else happy.</li>
      <li>More than that, your marriage isn’t for yourself, you’re marrying for a family.</li>
      <li>Not just for the in-laws and all of that nonsense, but for your future children.</li>
      <li>Who do you want to help you raise them?</li>
      <li>Who do you want to influence them?</li>
      <li>Marriage isn’t for you.</li>
      <li>It’s not about you.</li>
      <li>Marriage is about the person you married.</li>
    </ul>
  </section>

</main>
</body>
</html>
```